Business Card Design Project- Removalist

I would like to surprise my husband to be with a different type of wedding present. His brother (who he owned a removalist business with) suddenly passed away from cancer recently and he has changed his business name to 'RTB' (which stands for Raising Tom Bright; but the full name doesn't need to be on the business card as it is more of a personal business name). To celebrate the new business I would like to get him some business cards made.
I would like the business name to be listed as 'RTB' and somewhere on the card I would like 'Sydney wide removals and relocation services'. I would like it to be obvious from the front of the card that it is a removalist business card. If a truck or some other feature that makes it look like a removalist business card could added it would be appreciated.
I don't mind what colours are used, but I would like the colour blue to feature somewhere in the design. It can be bright and fun, which is how Tom was.
I will also need the company's email address and phone number listed
The email address is: rtbremovals@quillpost.example
The contact number is: 0417 282 934
I don't need a contact name listed on the card, but perhaps 'Owned and operated by the Pendleworth family' could be added near the contact details in small font.
Thank you very much for considering this project!
Kind regards,
Fiona
Updates
Could you please change the mobile contact number to 0417 282 934. This is the only contact phone number required on the card now.
Thank you!

```html
<!DOCTYPE html>
<html lang="en">
<head>
<meta charset="utf-8">
<title>RTB Removals – Business Cards</title>
<link rel="stylesheet" href="https://fonts.googleapis.com/css2?family=Jost:wght@400;500&family=Arimo&display=swap">
<style>
  :root {
    --backdrop: #1c1c1c;
    --card: #ffffff;
    --brand-blue: #1f5aa6;
    --band-dark: #233f8c;
    --band-light: #0f6cb8;
    --rule-grey: #7a7a7a;
    --tagline-grey: #666666;
    --contact-grey: #4a4a4a;
    --icon-blue: #1d5fa5;
    --photo-warm: #c9a57c;
    --photo-light: #ece4da;
  }
  * { margin: 0; padding: 0; box-sizing: border-box; }
  html, body {
    width: 1200px; height: 722px; overflow: hidden;
    background: var(--backdrop);
  }
  .canvas { position: relative; width: 1200px; height: 722px; }
  .card {
    position: absolute; width: 513px; height: 294px;
    border-radius: 12px; overflow: hidden; background: var(--card);
  }
  .card--front { left: 66px; top: 46px; }
  .card--back { left: 620px; top: 46px; }
  .card--photo { left: 287px; top: 373px; }

  .wordmark {
    font-family: "Jost", sans-serif; font-weight: 500;
    color: var(--brand-blue); line-height: 1; letter-spacing: 2px;
  }
  .card--front .wordmark {
    position: absolute; left: 42px; top: 52px; font-size: 132px;
  }
  .tagline {
    position: absolute; left: 37px; top: 173px;
    font-family: "Arimo", sans-serif; font-size: 12.5px; color: var(--tagline-grey);
  }
  .contacts {
    position: absolute; left: 44px; top: 209px;
    font-family: "Jost", sans-serif; font-size: 15.5px; color: var(--contact-grey);
    list-style: none;
  }
  .contacts li { display: flex; align-items: center; gap: 7px; height: 24px; }
  .contacts svg { width: 13px; height: 13px; flex: none; }
  .rule {
    position: absolute; left: 0; top: 257px; width: 100%; height: 3px;
    background: var(--rule-grey);
  }
  .owner-band {
    position: absolute; left: 0; top: 262px; width: 100%; height: 32px;
    background: linear-gradient(90deg, var(--band-dark), var(--band-light));
    color: #fff; font-family: "Jost", sans-serif; font-size: 17px;
    padding-left: 47px; line-height: 31px;
  }

  .card--back .wordmark,
  .card--photo .wordmark {
    position: absolute; left: 0; width: 100%; text-align: center; font-size: 132px;
  }
  .card--back .wordmark { top: 84px; }
  .photo-area {
    position: absolute; inset: 0;
    background: linear-gradient(100deg, var(--photo-warm) 0%, var(--photo-light) 45%, var(--photo-warm) 100%);
  }
  .card--photo .wordmark { top: 166px; color: #fff; }
</style>
</head>
<body>
<main class="canvas">
  <section class="card card--front">
    <div class="wordmark">RTB</div>
    <p class="tagline">Sydney Wide Removals &amp; Relocation Services</p>
    <ul class="contacts">
      <li>
        <svg viewBox="0 0 16 16" aria-hidden="true"><circle cx="8" cy="8" r="7" fill="none" stroke="var(--icon-blue)" stroke-width="1.5"/><path d="M5.5 4.5c-.5 2.5 1.5 6 4.5 7l1-1.5-1.8-1-.8.8c-1-.6-1.8-1.6-2-2.6l.9-.6-.6-2z" fill="var(--icon-blue)"/></svg>
        0417 282 934
      </li>
      <li>
        <svg viewBox="0 0 16 16" aria-hidden="true"><path d="M1 6l7-4 7 4v8H1z" fill="var(--icon-blue)"/><path d="M2.5 7l5.5 3.5L13.5 7" fill="none" stroke="#fff" stroke-width="1.3"/></svg>
        rtbremovals@quillpost.example
      </li>
    </ul>
    <div class="rule"></div>
    <div class="owner-band">Owned and operated by the Pendleworth family</div>
  </section>

  <section class="card card--back">
    <div class="wordmark">RTB</div>
  </section>

  <section class="card card--photo">
    <div class="photo-area" role="img" aria-label="Photo of a smiling couple sitting on the floor with glasses of wine among moving boxes, cushions and stacked plates"></div>
    <div class="wordmark">RTB</div>
  </section>
</main>
</body>
</html>
```